Veltora Software Business Card Design

We are a new organization called Veltora. We are a software as a service provider. We deliver a project and program management solution via the internet, so everyone has the ability to work together and collaborate. Its an enterprise platform and we will focus on 50 plus employee company.

We have a website in place
www.veltora-demo.com

Use this as a start of producing the business card. The logo is there as well, but if you have a great and better solution...

Color scheme's could be inline with the website, but don't pin point on it. We can always change the website, logo, color scheme etc.

Target Market(s)

B2B, Projectmembers, projectmanagers, ICT, CTO, Marketing Managers

Industry/Entity Type

Software

Requirements
Must have
• Marten Kuyvelsma

Tel: +31 255 47 09 36
Mob: +31 6 927 15 062
marten@veltora-demo.com
Oostelingpad 84c
2184 KT Nieuw Vennep

Www.veltora-demo.com
social media links

```html
<!DOCTYPE html>
<html lang="en">
<head>
<meta charset="utf-8">
<title>Veltora Business Card</title>
<link href="https://fonts.googleapis.com/css2?family=Open+Sans:wght@400;700&display=swap" rel="stylesheet">
<style>
  :root {
    --page-bg: #e6e7e9;
    --card-white: #f7f8f8;
    --corner-grey: #5b5d60;
    --corner-light: #eceeef;
    --band-dark: #2f3133;
    --band-mid: #6c6e71;
    --band-blue: #1f7fc0;
    --band-blue-dark: #14679f;
    --label-green: #7d9a2e;
    --text-grey: #4a4c4f;
    --text-white: #ffffff;
  }
  html, body {
    margin: 0;
    width: 1200px;
    height: 1000px;
    overflow: hidden;
    background: var(--page-bg);
  }
  .card {
    position: absolute;
    left: 150px;
    top: 230px;
    width: 900px;
    height: 540px;
    background: var(--card-white);
    box-shadow: 0 10px 30px rgba(0,0,0,0.18);
    overflow: hidden;
    font-family: "Open Sans", Arial, sans-serif;
  }
  .corner-strip {
    position: absolute;
    left: 0; top: 0;
    width: 900px; height: 48px;
  }
  .brand-area {
    position: absolute;
    left: 0; top: 48px;
    width: 100%; height: 170px;
    background: linear-gradient(180deg, #ffffff 0%, var(--corner-light) 100%);
    text-align: center;
  }
  .brand-name {
    margin: 0;
    padding-top: 34px;
    font-family: "Open Sans", Arial, sans-serif;
    font-weight: 400;
    font-size: 64px;
    line-height: 1;
    color: var(--text-grey);
  }
  .brand-web {
    margin: 26px 0 0;
    font-size: 22px;
    letter-spacing: 5px;
    color: var(--text-grey);
  }
  .name-band {
    position: absolute;
    left: 0; top: 218px;
    width: 100%; height: 118px;
    background: radial-gradient(ellipse at 55% 45%, var(--band-mid) 0%, var(--band-dark) 75%);
    text-align: center;
    color: var(--text-white);
  }
  .person-name {
    margin: 0;
    padding-top: 20px;
    font-size: 46px;
    font-weight: 700;
    letter-spacing: 4px;
    line-height: 1.1;
  }
  .person-email {
    margin: 6px 0 0;
    font-size: 20px;
    letter-spacing: 2px;
  }
  .contact-band {
    position: absolute;
    left: 0; top: 336px;
    width: 100%; height: 108px;
    background: linear-gradient(90deg, var(--band-blue-dark) 0%, var(--band-blue) 50%, var(--band-blue-dark) 100%);
    color: var(--text-white);
    font-size: 21px;
  }
  .contact-row {
    position: absolute;
    left: 0; width: 100%;
    display: flex;
    justify-content: center;
    gap: 90px;
  }
  .contact-row.phones { top: 20px; }
  .contact-row.address { top: 62px; }
  .social-strip {
    position: absolute;
    left: 0; top: 444px;
    width: 100%; height: 76px;
    background: var(--card-white);
  }
  .social-label {
    position: absolute;
    left: 560px; top: 8px;
    margin: 0;
    font-size: 19px;
    color: var(--label-green);
  }
  .social-icons {
    position: absolute;
    left: 620px; top: 38px;
  }
  .bottom-strip {
    position: absolute;
    left: 0; bottom: 0;
    width: 100%; height: 20px;
    background: var(--corner-grey);
  }
</style>
</head>
<body>
  <div class="card">
    <svg class="corner-strip" width="900" height="48" viewBox="0 0 900 48" aria-hidden="true">
      <rect width="900" height="48" fill="var(--corner-light)"/>
      <polygon points="0,0 900,0 820,48 0,48" fill="var(--corner-grey)"/>
    </svg>

    <header class="brand-area">
      <h1 class="brand-name">Veltora</h1>
      <p class="brand-web">Www.veltora-demo.com</p>
    </header>

    <section class="name-band">
      <h2 class="person-name">Marten Kuyvelsma</h2>
      <p class="person-email">marten@veltora-demo.com</p>
    </section>

    <section class="contact-band">
      <div class="contact-row phones">
        <span class="contact-tel">Tel: +31 255 47 09 36</span>
        <span class="contact-mob">Mob: +31 6 927 15 062</span>
      </div>
      <div class="contact-row address">
        <span class="contact-address">Oostelingpad 84c&nbsp;&nbsp;2184 KT Nieuw Vennep</span>
      </div>
    </section>

    <section class="social-strip">
      <p class="social-label">Find veltora on:</p>
      <svg class="social-icons" width="130" height="34" viewBox="0 0 130 34">
        <circle cx="17" cy="17" r="16" fill="var(--band-blue)" role="img" aria-label="Social network link"/>
        <circle cx="62" cy="17" r="16" fill="var(--band-blue)" role="img" aria-label="Social network link"/>
        <circle cx="107" cy="17" r="16" fill="var(--band-blue)" role="img" aria-label="Social network link"/>
      </svg>
    </section>

    <div class="bottom-strip"></div>
  </div>
</body>
</html>
```